PowerPoint Template Design for Management Consultancy

I need a PPT template for a new management consulting company. I want a modern look that uses dark blues and greys for divider slides, white content slides and a creative use of the logo in the slides. The supplied images are used on the website so I'd like to incorporate these into the theme

Target Market(s)

Management Consulting

Industry/Entity Type

Consulting

Font styles to use
Sans Serif

Colors
3277b5

Requirements
Must have
• Options for title slide, divider slides, content slides using the logo provided
Plain white content slides with creative use of logo
Color theme uses dark blues and greys
Nice to have
• Light and dark theme

```html
<!DOCTYPE html>
<html lang="en">
<head>
<meta charset="utf-8">
<title>Tessaro Advisory – Presentation Template</title>
<link href="https://fonts.googleapis.com/css2?family=Montserrat:wght@400;500;600;700&display=swap" rel="stylesheet">
<style>
:root{
  --bg:#c3c3c7;
  --navy:#1e3c6a;
  --blue:#3277b5;
  --sky:#5b95cc;
  --ink:#2b2d33;
  --grey:#393a3f;
  --muted:#6b6f78;
  --rule:#d9dde3;
  --paper:#ffffff;
}
*{box-sizing:border-box}
html,body{margin:0;padding:0}
body{width:1200px;height:3849px;overflow:hidden;background:var(--bg);font-family:'Montserrat',sans-serif;color:var(--ink);position:relative}
.slide{position:absolute;width:540px;height:304px;overflow:hidden;background:var(--paper)}
.hero{left:271px;top:85px;transform:scale(1.217);transform-origin:0 0;box-shadow:0 4px 18px rgba(0,0,0,.25)}
.col-l{left:52px}.col-r{left:610px}
.abs{position:absolute;margin:0}
.fill{position:absolute;inset:0}
.shape{position:absolute;inset:0;width:100%;height:100%}
.photo{position:absolute}
.ph-office{background:linear-gradient(120deg,#eef2f6 0%,#b9cbdd 30%,#5a82ae 55%,#2f5685 72%,#c7d6e6 100%)}
.ph-climb{background:linear-gradient(90deg,#efe6d6 0%,#dccdb3 38%,#a7a9a8 58%,#3a3a3c 72%,#141416 100%)}
.ph-summit{background:linear-gradient(180deg,#2c4d7c 0%,#7f96b3 45%,#eccb96 64%,#8c8a86 78%,#2a2b2e 100%)}
.ph-team{background:linear-gradient(90deg,#2d568a,#6e95c0 50%,#2d568a)}
.ph-target{background:linear-gradient(135deg,#e9e4de,#c9b8a6 50%,#d8c04a 70%,#8b8f96)}
.ph-hands{background:linear-gradient(135deg,#f4f6f9,#cfd9e4 45%,#8fa3b8 75%,#e8edf2)}
.ph-glass{background:linear-gradient(130deg,#eef3f8,#a8c2dc 40%,#e4ecf4 60%,#7fa2c6)}
.wordmark{position:absolute;left:40px;top:40px;font-weight:600;font-size:19px;color:var(--navy);line-height:1;margin:0}
.t-title{position:absolute;left:36px;top:142px;font-size:24px;font-weight:700;line-height:1.05;color:var(--navy);margin:0}
.t-sub{position:absolute;left:36px;top:208px;font-size:12px;font-weight:500;color:var(--ink);margin:0}
.t-date{position:absolute;left:36px;top:246px;font-size:5px;color:var(--ink);margin:0}
.dark .t-title,.dark .t-sub,.dark .t-date{color:#fff}
.copy{position:absolute;left:0;right:0;bottom:12px;text-align:center;font-size:4.8px;color:#fff;margin:0}
.foot-logo{position:absolute;left:18px;bottom:10px;font-size:9px;font-weight:600;color:var(--navy)}
.foot-logo.inv{color:#fff}
.pg{position:absolute;right:16px;bottom:10px;font-size:6px;color:var(--ink)}
.pg.inv{color:#fff}
.kicker{font-size:7px;color:var(--blue);margin:0}
.h2{font-size:17px;font-weight:700;color:var(--navy);margin:0;line-height:1.1}
.center{position:absolute;left:0;right:0;text-align:center;top:18px}
.body{font-size:5.2px;line-height:1.35;color:var(--ink);margin:0}
.body.inv{color:#fff}
.ico{fill:none;stroke:currentColor;stroke-width:1.8;stroke-linecap:round;stroke-linejoin:round}
.dot{position:absolute;border-radius:50%;background:var(--blue);color:#fff;display:flex;align-items:center;justify-content:center}
.dot svg{width:55%;height:55%}
.dot.ring{border:2px solid #fff}
.dot.dk{background:var(--grey)}
.toc-item{position:absolute;font-size:10px;color:var(--ink);display:flex;align-items:center;gap:12px}
.toc-item b{color:var(--blue);font-size:14px;font-weight:600;width:10px;text-align:right}
.card{position:absolute;background:#fff;padding:10px 12px}
.card h3{margin:0 0 4px;font-size:16px;font-weight:500;color:var(--blue)}
.member{position:absolute;top:75px;width:150px;text-align:center}
.avatar{width:60px;height:60px;border-radius:50%;margin:0 auto 8px;border:3px solid #fff;background:linear-gradient(160deg,#e7d9cc,#b79c86 60%,#5b6a80)}
.member h4{margin:0;font-size:8.5px;color:var(--blue);font-weight:600}
.member p.role{margin:1px 0 4px;font-size:6px;color:var(--blue)}
.sb-title{position:absolute;left:36px;font-size:22px;font-weight:700;color:#fff;margin:0}
.mark-square{position:absolute;left:38px;width:18px;height:18px;background:var(--navy)}
.svc-row{position:absolute;left:30px;display:flex;align-items:center;gap:12px;width:240px}
.svc-row .dot{position:relative;flex:0 0 22px;height:22px}
.grid-item{position:absolute;width:150px}
.grid-item h4{margin:0 0 2px;font-size:8px;font-weight:600;color:var(--ink)}
.grid-item.right{text-align:right}
.step{position:absolute;top:150px;width:90px;text-align:center}
.step h4{margin:0 0 3px;font-size:8px;font-weight:500}
.diamond{position:absolute;top:112px;width:32px;height:32px;transform:rotate(45deg);border:2px solid #fff;box-shadow:0 0 0 1px #cfd4db}
.diamond span{position:absolute;inset:0;display:flex;align-items:center;justify-content:center;transform:rotate(-45deg);color:#fff;font-size:15px;font-weight:500}
.tl{position:absolute;width:70px;text-align:center}
.tl b{display:block;font-size:10px;font-weight:500;color:var(--ink)}
.tl b.bl{color:var(--blue)}
.cyc-label{position:absolute;font-size:8px;line-height:1.05;color:var(--ink);margin:0}
table.data{position:absolute;left:25px;top:72px;width:490px;border-collapse:collapse;font-size:5.5px}
table.data th{background:var(--navy);color:#fff;font-weight:600;text-align:left;padding:5px 6px}
table.data th+th{text-align:center}
table.data td{padding:0 6px;height:28px;border-bottom:1px solid var(--rule)}
table.data td+td{text-align:center;color:var(--blue);font-size:8px}
table.data td:last-child{color:var(--ink)}
.legend{position:absolute;left:358px;width:160px}
.legend h4{margin:0 0 2px;font-size:7px;font-weight:500;color:var(--blue);display:flex;align-items:center;gap:5px}
.legend h4 i{width:7px;height:7px;border-radius:50%;background:var(--blue);display:inline-block}
.legend h4.alt{color:var(--ink)}
.legend h4.alt i{background:var(--grey)}
.contact{position:absolute;left:36px;top:165px;color:#fff}
.contact h3{margin:0 0 12px;font-size:13px;font-weight:500}
.contact p{margin:0 0 4px;font-size:6px;display:flex;align-items:center;gap:6px}
.contact svg{width:8px;height:8px}
</style>
</head>
<body>

<svg width="0" height="0" style="position:absolute" aria-hidden="true">
  <symbol id="i-search" viewBox="0 0 24 24"><circle cx="10" cy="10" r="6"/><path d="M14.5 14.5 20 20"/></symbol>
  <symbol id="i-bulb" viewBox="0 0 24 24"><path d="M9 18h6M10 21h4M12 3a6 6 0 0 0-4 10.5c.7.7 1 1.5 1 2.5h6c0-1 .3-1.8 1-2.5A6 6 0 0 0 12 3z"/></symbol>
  <symbol id="i-list" viewBox="0 0 24 24"><rect x="5" y="4" width="14" height="16" rx="2"/><path d="M8 9h8M8 13h8M8 17h5"/></symbol>
  <symbol id="i-user" viewBox="0 0 24 24"><circle cx="12" cy="8" r="4"/><path d="M5 20c0-4 3-6 7-6s7 2 7 6"/></symbol>
  <symbol id="i-screen" viewBox="0 0 24 24"><rect x="3" y="4" width="18" height="12" rx="1"/><path d="M9 20h6M12 16v4"/></symbol>
  <symbol id="i-doc" viewBox="0 0 24 24"><path d="M6 3h9l4 4v14H6z"/><path d="M9 12h7M9 16h7"/></symbol>
  <symbol id="i-gear" viewBox="0 0 24 24"><circle cx="12" cy="12" r="3"/><circle cx="12" cy="12" r="7.5" stroke-dasharray="3 2.2"/></symbol>
  <symbol id="i-cal" viewBox="0 0 24 24"><rect x="4" y="5" width="16" height="15" rx="1"/><path d="M4 10h16M8 3v4M16 3v4M8 14h2M12 14h2M16 14h1M8 17h2M12 17h2"/></symbol>
  <symbol id="i-flag" viewBox="0 0 24 24"><path d="M6 21V4h11l-2 4 2 4H6"/></symbol>
  <symbol id="i-clock" viewBox="0 0 24 24"><circle cx="12" cy="12" r="8"/><path d="M12 8v4l3 2"/></symbol>
  <symbol id="i-chart" viewBox="0 0 24 24"><path d="M5 19v-6M10 19V8M15 19v-4M20 19V5"/></symbol>
  <symbol id="i-phone" viewBox="0 0 24 24"><path d="M5 4h4l2 5-3 2a11 11 0 0 0 5 5l2-3 5 2v4a2 2 0 0 1-2 2A16 16 0 0 1 3 6a2 2 0 0 1 2-2z"/></symbol>
  <symbol id="i-mail" viewBox="0 0 24 24"><rect x="3" y="5" width="18" height="14" rx="1"/><path d="m3 6 9 7 9-7"/></symbol>
  <symbol id="i-globe" viewBox="0 0 24 24"><circle cx="12" cy="12" r="9"/><path d="M3 12h18M12 3c3 3 3 15 0 18M12 3c-3 3-3 15 0 18"/></symbol>
</svg>

<!-- Featured title slide -->
<section class="slide hero">
  <div class="photo ph-office fill" role="img" aria-label="Business person writing notes at a desk, tinted blue"></div>
  <svg class="shape" viewBox="0 0 540 304" aria-hidden="true">
    <polygon points="300,0 370,0 470,270 400,270" fill="#fff" opacity=".18"/>
    <polygon points="0,128 300,128 380,270 0,270" fill="var(--navy)"/>
    <polygon points="395,270 425,270 410,288" fill="var(--blue)"/>
    <rect x="0" y="270" width="540" height="34" fill="var(--grey)"/>
  </svg>
  <p class="wordmark">Tessaro Advisory</p>
  <div class="dark">
    <h1 class="t-title">Presentation Title<br>Goes Here!</h1>
    <p class="t-sub">Subtitle of Presentation</p>
    <p class="t-date">Monday, May 3, 2021</p>
  </div>
  <p class="copy">Copyright © 2021 Tessaro Advisory · All Rights Reserved</p>
</section>

<!-- Title, light, office -->
<section class="slide col-l" style="top:595px">
  <div class="photo ph-office fill" role="img" aria-label="Business person writing notes at a desk"></div>
  <svg class="shape" viewBox="0 0 540 304" aria-hidden="true">
    <polygon points="300,0 370,0 470,270 400,270" fill="#fff" opacity=".18"/>
    <polygon points="0,128 300,128 380,270 0,270" fill="#fff"/>
    <polygon points="395,270 425,270 410,288" fill="var(--blue)"/>
    <rect x="0" y="270" width="540" height="34" fill="var(--grey)"/>
  </svg>
  <p class="wordmark">Tessaro Advisory</p>
  <h1 class="t-title">Presentation Title<br>Goes Here!</h1>
  <p class="t-sub">Subtitle of Presentation</p>
  <p class="t-date">Monday, May 3, 2021</p>
  <p class="copy">Copyright © 2021 Tessaro Advisory · All Rights Reserved</p>
</section>

<!-- Title, light, climber -->
<section class="slide col-r" style="top:595px">
  <div class="photo ph-climb fill" role="img" aria-label="Climbers silhouetted on a mountain ridge at sunrise"></div>
  <svg class="shape" viewBox="0 0 540 304" aria-hidden="true">
    <polygon points="260,0 320,0 430,270 370,270" fill="#fff" opacity=".22"/>
    <polygon points="0,128 300,128 380,270 0,270" fill="#fff"/>
    <polygon points="395,270 425,270 410,288" fill="var(--blue)"/>
    <rect x="0" y="270" width="540" height="34" fill="var(--grey)"/>
  </svg>
  <p class="wordmark">Tessaro Advisory</p>
  <h1 class="t-title">Presentation Title<br>Goes Here!</h1>
  <p class="t-sub">Subtitle of Presentation</p>
  <p class="t-date">Monday, May 3, 2021</p>
  <p class="copy">Copyright © 2021 Tessaro Advisory · All Rights Reserved</p>
</section>

<!-- Title, dark, office -->
<section class="slide col-l dark" style="top:916px">
  <div class="photo ph-office fill" role="img" aria-label="Business person writing notes at a desk, tinted blue"></div>
  <svg class="shape" viewBox="0 0 540 304" aria-hidden="true">
    <polygon points="300,0 370,0 470,270 400,270" fill="#fff" opacity=".18"/>
    <polygon points="0,128 300,128 380,270 0,270" fill="var(--navy)"/>
    <polygon points="395,270 425,270 410,288" fill="var(--blue)"/>
    <rect x="0" y="270" width="540" height="34" fill="var(--grey)"/>
  </svg>
  <p class="wordmark">Tessaro Advisory</p>
  <h1 class="t-title">Presentation Title<br>Goes Here!</h1>
  <p class="t-sub">Subtitle of Presentation</p>
  <p class="t-date">Monday, May 3, 2021</p>
  <p class="copy">Copyright © 2021 Tessaro Advisory · All Rights Reserved</p>
</section>

<!-- Title, dark, summit -->
<section class="slide col-r dark" style="top:916px">
  <div class="photo ph-summit fill" role="img" aria-label="Two hikers celebrating on a summit at sunset"></div>
  <svg class="shape" viewBox="0 0 540 304" aria-hidden="true">
    <polygon points="300,0 370,0 470,270 400,270" fill="#fff" opacity=".15"/>
    <polygon points="0,128 300,128 380,270 0,270" fill="var(--navy)"/>
    <polygon points="395,270 425,270 410,288" fill="var(--blue)"/>
    <rect x="0" y="270" width="540" height="34" fill="var(--grey)"/>
  </svg>
  <p class="wordmark">Tessaro Advisory</p>
  <h1 class="t-title">Presentation Title<br>Goes Here!</h1>
  <p class="t-sub">Subtitle of Presentation</p>
  <p class="t-date">Monday, May 3, 2021</p>
  <p class="copy">Copyright © 2021 Tessaro Advisory · All Rights Reserved</p>
</section>

<!-- Table of contents -->
<section class="slide col-l" style="top:1237px">
  <div class="center"><p class="kicker">Table of</p><h2 class="h2">Contents</h2></div>
  <div class="toc-item" style="left:60px;top:92px"><b>1</b>Title Goes Here!</div>
  <div class="toc-item" style="left:280px;top:92px"><b>2</b>Title Goes Here!</div>
  <div class="toc-item" style="left:60px;top:135px"><b>3</b>Title Goes Here!</div>
  <div class="toc-item" style="left:280px;top:135px"><b>4</b>Title Goes Here!</div>
  <div class="toc-item" style="left:60px;top:178px"><b>5</b>Title Goes Here!</div>
  <div class="toc-item" style="left:280px;top:178px"><b>6</b>Title Goes Here!</div>
  <div class="toc-item" style="left:60px;top:221px"><b>7</b>Title Goes Here!</div>
  <div class="toc-item" style="left:280px;top:221px"><b>8</b>Title Goes Here!</div>
  <span class="foot-logo">Tessaro</span><span class="pg">5</span>
</section>

<!-- Who we are -->
<section class="slide col-r" style="top:1237px">
  <div class="photo ph-climb" style="left:0;top:0;width:540px;height:180px" role="img" aria-label="Climbers on a rocky peak above a misty valley"></div>
  <div class="abs" style="left:0;top:180px;width:540px;height:124px;background:var(--navy)"></div>
  <div class="dot ring" style="left:50px;top:170px;width:36px;height:36px"><svg class="ico"><use href="#i-search"/></svg></div>
  <div class="dot ring" style="left:125px;top:170px;width:36px;height:36px"><svg class="ico"><use href="#i-bulb"/></svg></div>
  <div class="dot ring" style="left:200px;top:170px;width:36px;height:36px"><svg class="ico"><use href="#i-list"/></svg></div>
  <div class="card" style="left:290px;top:45px;width:205px;height:210px;text-align:center;padding-top:28px">
    <p class="kicker">About Us</p>
    <h2 class="h2" style="font-weight:500;color:var(--blue);margin-bottom:8px">Who We Are</h2>
    <p class="body" style="font-size:6px">Lorem ipsum dolor sit amet, at laborum nibh duis mauris. Per ultrices lectus sed metus tristique eu. Diam suspendisse ac ipsum maecenas fermentum, aliquet imperdiet et lobortis venenatis nascetur lacus. A ac, vivamus erat nullam. Eu adipiscing pulvinar eros. Mollis malesuada vel scelerisque, ligula quam non mauris.</p>
  </div>
  <span class="foot-logo inv">Tessaro</span><span class="pg inv">| 6</span>
</section>

<!-- Mission & values -->
<section class="slide col-l" style="top:1558px">
  <div class="photo ph-summit" style="left:0;top:0;width:340px;height:304px" role="img" aria-label="Two hikers with raised arms on a summit at sunset"></div>
  <div class="abs" style="left:340px;top:0;width:200px;height:304px;background:var(--navy)"></div>
  <div class="card" style="left:205px;top:40px;width:290px;height:88px">
    <h3>Our Mission</h3>
    <p class="body">Lorem ipsum dolor sit amet, at laborum nibh duis mauris. Per ultrices lectus sed metus tristique eu. Diam suspendisse ac ipsum maecenas fermentum, aliquet imperdiet et lobortis venenatis nascetur lacus. A ac, vivamus erat nullam. Eu adipiscing pulvinar eros. Mollis malesuada vel scelerisque, ligula quam non mauris neque eleifend etiam.</p>
  </div>
  <div class="card" style="left:205px;top:155px;width:290px;height:92px">
    <h3>Our Values</h3>
    <p class="body">Lorem ipsum dolor sit amet, at laborum nibh duis mauris. Per ultrices lectus sed metus tristique eu. Diam suspendisse ac ipsum maecenas fermentum, aliquet imperdiet et lobortis venenatis nascetur lacus. A ac, vivamus erat nullam. Eu adipiscing pulvinar eros. Mollis malesuada vel scelerisque, ligula quam non mauris neque eleifend etiam.</p>
  </div>
  <span class="foot-logo inv">Tessaro</span><span class="pg inv">| 7</span>
</section>

<!-- Our value -->
<section class="slide col-r" style="top:1558px">
  <div class="center"><p class="kicker">About Us</p><h2 class="h2">Our Value</h2></div>
  <div class="abs" style="left:220px;top:102px;width:320px;height:95px;background:var(--navy)"></div>
  <div class="photo ph-target" style="left:35px;top:90px;width:190px;height:125px" role="img" aria-label="Hand placing a dart on a target beside a laptop"></div>
  <p class="body inv abs" style="left:250px;top:118px;width:260px;font-size:7px">Lorem ipsum dolor sit amet, at laborum nibh duis mauris. Per ultrices lectus sed metus tristique eu. Diam suspendisse ac ipsum maecenas fermentum, aliquet imperdiet et lobortis venenatis nascetur lacus. A ac, vivamus erat nullam. Eu adipiscing pulvinar eros.</p>
  <p class="abs" style="left:250px;top:208px;font-size:9px;color:var(--blue)">Title Goes Here!</p>
  <ul class="body abs" style="left:250px;top:222px;width:260px;padding-left:10px">
    <li>Lorem ipsum dolor sit amet, at laborum nibh duis mauris. Per ultrices lectus sed metus tristique eu.</li>
    <li>Diam suspendisse ac ipsum maecenas fermentum, aliquet imperdiet et lobortis venenatis nascetur lacus.</li>
  </ul>
  <span class="foot-logo">Tessaro</span><span class="pg">8</span>
</section>

<!-- Team -->
<section class="slide col-l" style="top:1880px">
  <div class="photo ph-team" style="left:0;top:0;width:540px;height:115px" role="img" aria-label="Silhouettes of a business team in a bright office, tinted blue"></div>
  <div class="center"><p class="kicker" style="color:#fff">Meet Our</p><h2 class="h2" style="color:#fff">TEAM</h2></div>
  <div class="member" style="left:30px"><div class="avatar" role="img" aria-label="Portrait of a team member"></div><h4>Name Goes Here!</h4><p class="role">Job Title Goes Here!</p><p class="body">Lorem ipsum dolor sit amet, at laborum nibh duis mauris. Per ultrices lectus sed metus tristique eu. Diam suspendisse ac ipsum maecenas fermentum, aliquet imperdiet et lobortis venenatis nascetur lacus. A ac, vivamus erat nullam.</p></div>
  <div class="member" style="left:195px"><div class="avatar" role="img" aria-label="Portrait of a team member"></div><h4>Name Goes Here!</h4><p class="role">Job Title Goes Here!</p><p class="body">Lorem ipsum dolor sit amet, at laborum nibh duis mauris. Per ultrices lectus sed metus tristique eu. Diam suspendisse ac ipsum maecenas fermentum, aliquet imperdiet et lobortis venenatis nascetur lacus. A ac, vivamus erat nullam.</p></div>
  <div class="member" style="left:360px"><div class="avatar" role="img" aria-label="Portrait of a team member"></div><h4>Name Goes Here!</h4><p class="role">Job Title Goes Here!</p><p class="body">Lorem ipsum dolor sit amet, at laborum nibh duis mauris. Per ultrices lectus sed metus tristique eu. Diam suspendisse ac ipsum maecenas fermentum, aliquet imperdiet et lobortis venenatis nascetur lacus. A ac, vivamus erat nullam.</p></div>
  <span class="foot-logo">Tessaro</span><span class="pg">9</span>
</section>

<!-- Section break, climber -->
<section class="slide col-r" style="top:1880px">
  <div class="photo ph-climb fill" role="img" aria-label="Climbers on a rocky peak above a misty valley"></div>
  <svg class="shape" viewBox="0 0 540 304" aria-hidden="true">
    <polygon points="0,135 330,135 395,270 0,270" fill="var(--navy)"/>
    <polygon points="395,270 425,270 410,288" fill="var(--blue)"/>
    <rect x="0" y="270" width="540" height="34" fill="var(--grey)"/>
  </svg>
  <div class="mark-square" style="top:70px"></div>
  <h2 class="sb-title" style="top:160px">Section Break</h2>
  <p class="body inv abs" style="left:36px;top:196px;width:270px;font-size:7px">Lorem ipsum dolor sit amet, at laborum nibh duis mauris. Per ultrices lectus sed metus tristique eu. Diam suspendisse ac ipsum maecenas fermentum, aliquet imperdiet et lobortis venenatis.</p>
</section>

<!-- Services list -->
<section class="slide col-l" style="top:2201px">
  <div class="photo ph-hands" style="left:290px;top:0;width:250px;height:304px" role="img" aria-label="Colleagues reviewing printed charts together"></div>
  <div class="abs" style="left:30px;top:28px"><p class="kicker">Our Services</p><h2 class="h2">Slide Title Goes Here!</h2></div>
  <div class="svc-row" style="top:88px"><span class="dot"><svg class="ico"><use href="#i-bulb"/></svg></span><p class="body">Lorem ipsum dolor sit amet, at laborum nibh duis mauris. Per ultrices lectus sed metus. Lorem ipsum dolor sit amet.</p></div>
  <div class="svc-row" style="top:130px"><span class="dot"><svg class="ico"><use href="#i-search"/></svg></span><p class="body">Lorem ipsum dolor sit amet, at laborum nibh duis mauris. Per ultrices lectus sed metus. Lorem ipsum dolor sit amet.</p></div>
  <div class="svc-row" style="top:172px"><span class="dot"><svg class="ico"><use href="#i-user"/></svg></span><p class="body">Lorem ipsum dolor sit amet, at laborum nibh duis mauris. Per ultrices lectus sed metus. Lorem ipsum dolor sit amet.</p></div>
  <div class="svc-row" style="top:214px"><span class="dot"><svg class="ico"><use href="#i-gear"/></svg></span><p class="body">Lorem ipsum dolor sit amet, at laborum nibh duis mauris. Per ultrices lectus sed metus. Lorem ipsum dolor sit amet.</p></div>
  <span class="foot-logo">Tessaro</span><span class="pg">11</span>
</section>

<!-- Services grid -->
<section class="slide col-r" style="top:2201px">
  <div class="center"><p class="kicker">Our Services</p><h2 class="h2">Slide Title Goes Here!</h2></div>
  <div class="grid-item right" style="left:55px;top:90px"><h4>Title Goes Here!</h4><p class="body">Lorem ipsum dolor sit amet, at laborum nibh duis mauris. Per ultrices lectus sed metus. Lorem ipsum dolor sit amet.</p></div>
  <div class="grid-item right" style="left:55px;top:147px"><h4>Title Goes Here!</h4><p class="body">Lorem ipsum dolor sit amet, at laborum nibh duis mauris. Per ultrices lectus sed metus. Lorem ipsum dolor sit amet.</p></div>
  <div class="grid-item right" style="left:55px;top:204px"><h4>Title Goes Here!</h4><p class="body">Lorem ipsum dolor sit amet, at laborum nibh duis mauris. Per ultrices lectus sed metus. Lorem ipsum dolor sit amet.</p></div>
  <div class="dot" style="left:216px;top:88px;width:34px;height:34px"><svg class="ico"><use href="#i-bulb"/></svg></div>
  <div class="dot" style="left:278px;top:88px;width:34px;height:34px"><svg class="ico"><use href="#i-search"/></svg></div>
  <div class="dot" style="left:216px;top:145px;width:34px;height:34px"><svg class="ico"><use href="#i-list"/></svg></div>
  <div class="dot" style="left:278px;top:145px;width:34px;height:34px"><svg class="ico"><use href="#i-user"/></svg></div>
  <div class="dot" style="left:216px;top:202px;width:34px;height:34px"><svg class="ico"><use href="#i-screen"/></svg></div>
  <div class="dot" style="left:278px;top:202px;width:34px;height:34px"><svg class="ico"><use href="#i-doc"/></svg></div>
  <div class="grid-item" style="left:328px;top:90px"><h4>Title Goes Here!</h4><p class="body">Lorem ipsum dolor sit amet, at laborum nibh duis mauris. Per ultrices lectus sed metus. Lorem ipsum dolor sit amet.</p></div>
  <div class="grid-item" style="left:328px;top:147px"><h4>Title Goes Here!</h4><p class="body">Lorem ipsum dolor sit amet, at laborum nibh duis mauris. Per ultrices lectus sed metus. Lorem ipsum dolor sit amet.</p></div>
  <div class="grid-item" style="left:328px;top:204px"><h4>Title Goes Here!</h4><p class="body">Lorem ipsum dolor sit amet, at laborum nibh duis mauris. Per ultrices lectus sed metus. Lorem ipsum dolor sit amet.</p></div>
  <span class="foot-logo">Tessaro</span><span class="pg">12</span>
</section>

<!-- Process -->
<section class="slide col-l" style="top:2523px">
  <div class="center"><p class="kicker">Our Process</p><h2 class="h2">Slide Title Goes Here!</h2></div>
  <div class="abs" style="left:35px;top:100px;width:145px">
    <h3 style="margin:0 0 8px;font-size:16px;font-weight:500;line-height:1.05">Title Goes<br>Here!</h3>
    <p class="body" style="font-size:6px">Lorem ipsum dolor sit amet, at laborum nibh duis mauris. Per ultrices lectus sed metus tristique eu. Diam suspendisse ac ipsum maecenas fermentum, aliquet imperdiet et lobortis.</p>
  </div>
  <svg class="shape" viewBox="0 0 540 304" aria-hidden="true">
    <polygon points="250,116 300,116 314,128 300,140 250,140" fill="#e3e6ea"/>
    <polygon points="355,116 405,116 419,128 405,140 355,140" fill="#e3e6ea"/>
  </svg>
  <div class="diamond" style="left:226px;background:var(--blue)"><span>1</span></div>
  <div class="diamond" style="left:331px;background:var(--grey)"><span>2</span></div>
  <div class="diamond" style="left:436px;background:var(--navy)"><span>3</span></div>
  <div class="step" style="left:197px"><h4>Heading</h4><p class="body">Lorem ipsum dolor sit amet, at laborum nibh duis mauris. Per ultrices lectus sed metus tristique eu. Diam suspendisse.</p></div>
  <div class="step" style="left:302px"><h4>Heading</h4><p class="body">Lorem ipsum dolor sit amet, at laborum nibh duis mauris. Per ultrices lectus sed metus tristique eu. Diam suspendisse.</p></div>
  <div class="step" style="left:407px"><h4>Heading</h4><p class="body">Lorem ipsum dolor sit amet, at laborum nibh duis mauris. Per ultrices lectus sed metus tristique eu. Diam suspendisse.</p></div>
  <span class="foot-logo">Tessaro</span><span class="pg">13</span>
</section>

<!-- Section break, summit -->
<section class="slide col-r" style="top:2523px">
  <div class="photo ph-summit fill" role="img" aria-label="Two hikers celebrating on a summit at sunset"></div>
  <svg class="shape" viewBox="0 0 540 304" aria-hidden="true">
    <polygon points="260,0 320,0 430,270 370,270" fill="#fff" opacity=".2"/>
    <polygon points="0,135 330,135 395,270 0,270" fill="#fff"/>
    <polygon points="395,270 425,270 410,288" fill="var(--blue)"/>
    <rect x="0" y="270" width="540" height="34" fill="var(--grey)"/>
  </svg>
  <div class="mark-square" style="top:70px"></div>
  <h2 class="sb-title" style="top:160px;color:var(--navy)">Section Break</h2>
  <p class="body abs" style="left:36px;top:196px;width:270px;font-size:7px">Lorem ipsum dolor sit amet, at laborum nibh duis mauris. Per ultrices lectus sed metus tristique eu. Diam suspendisse ac ipsum maecenas fermentum, aliquet imperdiet et lobortis venenatis.</p>
</section>

<!-- Timeline -->
<section class="slide col-l" style="top:2845px">
  <div class="center"><p class="kicker">Business</p><h2 class="h2">Timeline</h2></div>
  <svg class="shape" viewBox="0 0 540 304" aria-hidden="true">
    <rect x="0" y="148" width="540" height="9" fill="#c9ccd2"/>
    <rect x="53" y="148" width="70" height="9" fill="var(--blue)"/>
    <rect x="144" y="148" width="70" height="9" fill="var(--grey)"/>
    <rect x="234" y="148" width="70" height="9" fill="var(--blue)"/>
    <rect x="324" y="148" width="70" height="9" fill="var(--grey)"/>
    <rect x="414" y="148" width="70" height="9" fill="var(--grey)"/>
  </svg>
  <div class="dot" style="left:72px;top:98px;width:32px;height:32px"><svg class="ico"><use href="#i-user"/></svg></div>
  <div class="dot" style="left:253px;top:98px;width:32px;height:32px;background:var(--navy)"><svg class="ico"><use href="#i-list"/></svg></div>
  <div class="dot dk" style="left:433px;top:98px;width:32px;height:32px"><svg class="ico"><use href="#i-cal"/></svg></div>
  <div class="dot dk" style="left:163px;top:172px;width:32px;height:32px"><svg class="ico"><use href="#i-bulb"/></svg></div>
  <div class="dot" style="left:343px;top:172px;width:32px;height:32px"><svg class="ico"><use href="#i-flag"/></svg></div>
  <div class="tl" style="left:144px;top:78px"><p class="body">Lorem ipsum dolor sit amet, at laborum nibh duis mauris. Per ultrices lectus sed metus tristique eu.</p><b>2018</b></div>
  <div class="tl" style="left:324px;top:78px"><p class="body">Lorem ipsum dolor sit amet, at laborum nibh duis mauris. Per ultrices lectus sed metus tristique eu.</p><b class="bl">2020</b></div>
  <div class="tl" style="left:53px;top:162px"><b class="bl">2017</b><p class="body">Lorem ipsum dolor sit amet, at laborum nibh duis mauris. Per ultrices lectus sed metus tristique eu.</p></div>
  <div class="tl" style="left:234px;top:162px"><b>2019</b><p class="body">Lorem ipsum dolor sit amet, at laborum nibh duis mauris. Per ultrices lectus sed metus tristique eu.</p></div>
  <div class="tl" style="left:414px;top:162px"><b>2021</b><p class="body">Lorem ipsum dolor sit amet, at laborum nibh duis mauris. Per ultrices lectus sed metus tristique eu.</p></div>
  <span class="foot-logo">Tessaro</span><span class="pg">15</span>
</section>

<!-- Cycle diagram -->
<section class="slide col-r" style="top:2845px">
  <div class="abs" style="left:40px;top:75px;width:150px;text-align:center">
    <p class="kicker">Heading</p>
    <h2 class="h2" style="margin-bottom:10px">Title Goes<br>Here!</h2>
    <p class="body" style="font-size:6px">Lorem ipsum dolor sit amet, at laborum nibh duis mauris. Per ultrices lectus sed metus tristique eu. Diam suspendisse ac ipsum maecenas fermentum, aliquet imperdiet et lobortis venenatis nascetur lacus. A ac, vivamus erat nullam.</p>
  </div>
  <svg class="shape" viewBox="0 0 540 304" aria-hidden="true">
    <path d="M305 78 A75 75 0 0 1 305 228" fill="none" stroke="var(--blue)" stroke-width="8"/>
    <path d="M305 78 A75 75 0 0 0 290 79.5" fill="none" stroke="var(--navy)" stroke-width="8"/>
    <path d="M305 228 A75 75 0 0 1 290 226.5" fill="none" stroke="var(--navy)" stroke-width="8"/>
    <circle cx="305" cy="153" r="55" fill="var(--navy)"/>
  </svg>
  <p class="abs" style="left:250px;top:130px;width:110px;text-align:center;color:#fff;font-size:13px;line-height:1.05">Heading<br>Goes<br>Here!</p>
  <div class="dot dk ring" style="left:337px;top:80px;width:28px;height:28px"><svg class="ico"><use href="#i-list"/></svg></div>
  <div class="dot dk ring" style="left:366px;top:122px;width:28px;height:28px"><svg class="ico"><use href="#i-search"/></svg></div>
  <div class="dot dk ring" style="left:366px;top:176px;width:28px;height:28px"><svg class="ico"><use href="#i-clock"/></svg></div>
  <div class="dot dk ring" style="left:337px;top:218px;width:28px;height:28px"><svg class="ico"><use href="#i-chart"/></svg></div>
  <p class="cyc-label" style="left:372px;top:84px">Heading<br>Goes Here!</p>
  <p class="cyc-label" style="left:402px;top:126px">Heading<br>Goes Here!</p>
  <p class="cyc-label" style="left:402px;top:180px">Heading<br>Goes Here!</p>
  <p class="cyc-label" style="left:372px;top:222px">Heading<br>Goes Here!</p>
  <span class="foot-logo">Tessaro</span><span class="pg">16</span>
</section>

<!-- Chart -->
<section class="slide col-l" style="top:3166px">
  <div class="center"><p class="kicker">Chart Slide</p><h2 class="h2">Slide Title Goes Here!</h2></div>
  <svg class="shape" viewBox="0 0 540 304" aria-hidden="true" font-family="Montserrat, sans-serif" font-size="5" fill="var(--muted)">
    <g stroke="#e3e6ea" stroke-width=".6">
      <line x1="55" y1="75" x2="320" y2="75"/><line x1="55" y1="96" x2="320" y2="96"/><line x1="55" y1="117" x2="320" y2="117"/>
      <line x1="55" y1="138" x2="320" y2="138"/><line x1="55" y1="159" x2="320" y2="159"/><line x1="55" y1="180" x2="320" y2="180"/>
    </g>
    <line x1="55" y1="201" x2="320" y2="201" stroke="#aab0b8" stroke-width=".8"/>
    <text x="45" y="77">6</text><text x="45" y="98">5</text><text x="45" y="119">4</text><text x="45" y="140">3</text><text x="45" y="161">2</text><text x="45" y="182">1</text><text x="45" y="203">0</text>
    <rect x="68" y="110" width="10" height="91" fill="var(--blue)"/><rect x="81" y="155" width="10" height="46" fill="var(--grey)"/>
    <rect x="132" y="128" width="10" height="73" fill="var(--blue)"/><rect x="145" y="98" width="10" height="103" fill="var(--grey)"/>
    <rect x="196" y="125" width="10" height="76" fill="var(--blue)"/><rect x="209" y="155" width="10" height="46" fill="var(--grey)"/>
    <rect x="260" y="106" width="10" height="95" fill="var(--blue)"/><rect x="273" y="98" width="10" height="103" fill="var(--grey)"/>
    <text x="68" y="212">Category 1</text><text x="132" y="212">Category 2</text><text x="196" y="212">Category 3</text><text x="260" y="212">Category 4</text>
  </svg>
  <div class="legend" style="top:80px"><h4><i></i>Title Goes Here!</h4><p class="body">Lorem ipsum dolor sit amet, at laborum nibh duis mauris. Per ultrices lectus sed metus tristique eu.</p></div>
  <div class="legend" style="top:132px"><h4 class="alt"><i></i>Title Goes Here!</h4><p class="body">Lorem ipsum dolor sit amet, at laborum nibh duis mauris. Per ultrices lectus sed metus tristique eu.</p></div>
  <div class="legend" style="top:184px"><h4><i></i>Title Goes Here!</h4><p class="body">Lorem ipsum dolor sit amet, at laborum nibh duis mauris. Per ultrices lectus sed metus tristique eu.</p></div>
  <span class="foot-logo">Tessaro</span><span class="pg">17</span>
</section>

<!-- Table -->
<section class="slide col-r" style="top:3166px">
  <div class="center"><p class="kicker">Table Slide</p><h2 class="h2">Slide Title Goes Here!</h2></div>
  <table class="data">
    <thead><tr><th>Heading</th><th>Heading 1</th><th>Heading 2</th><th>Heading 3</th><th>Heading 4</th><th>Heading 5</th></tr></thead>
    <tbody>
      <tr><td>Lorem ipsum dolor sit amet ...</td><td>✓</td><td>✓</td><td>✓</td><td>✓</td><td>✓</td></tr>
      <tr><td>Lorem ipsum dolor sit amet ...</td><td></td><td>✓</td><td>✓</td><td>✓</td><td>✓</td></tr>
      <tr><td>Lorem ipsum dolor sit amet ...</td><td></td><td></td><td>✓</td><td>✓</td><td>✓</td></tr>
      <tr><td>Lorem ipsum dolor sit amet ...</td><td></td><td></td><td></td><td>✓</td><td>✓</td></tr>
      <tr><td>Lorem ipsum dolor sit amet ...</td><td></td><td></td><td></td><td></td><td>✓</td></tr>
    </tbody>
  </table>
  <span class="foot-logo">Tessaro</span><span class="pg">18</span>
</section>

<!-- Contact, glass -->
<section class="slide col-l" style="top:3489px">
  <div class="photo ph-glass fill" role="img" aria-label="Modern glass office building facade"></div>
  <svg class="shape" viewBox="0 0 540 304" aria-hidden="true">
    <polygon points="0,135 300,135 380,270 0,270" fill="var(--navy)"/>
    <polygon points="380,135 540,135 540,270 460,270" fill="var(--navy)" opacity=".85"/>
    <rect x="0" y="270" width="540" height="34" fill="var(--grey)"/>
  </svg>
  <p class="wordmark">Tessaro Advisory</p>
  <div class="contact">
    <h3>Contact Us</h3>
    <p><svg class="ico"><use href="#i-phone"/></svg>555-0142-7788</p>
    <p><svg class="ico"><use href="#i-mail"/></svg>hello@tessaro-advisory.com</p>
    <p><svg class="ico"><use href="#i-globe"/></svg>www.tessaro-advisory.com</p>
  </div>
  <p class="copy">Copyright © 2021 Tessaro Advisory · All Rights Reserved</p>
</section>

<!-- Contact, handshake -->
<section class="slide col-r" style="top:3489px">
  <div class="photo ph-hands fill" role="img" aria-label="Two business people shaking hands"></div>
  <svg class="shape" viewBox="0 0 540 304" aria-hidden="true">
    <polygon points="0,135 300,135 380,270 0,270" fill="var(--navy)"/>
    <polygon points="380,135 540,135 540,270 460,270" fill="var(--navy)" opacity=".85"/>
    <rect x="0" y="270" width="540" height="34" fill="var(--grey)"/>
  </svg>
  <p class="wordmark">Tessaro Advisory</p>
  <div class="contact">
    <h3>Contact Us</h3>
    <p><svg class="ico"><use href="#i-phone"/></svg>555-0142-7788</p>
    <p><svg class="ico"><use href="#i-mail"/></svg>hello@tessaro-advisory.com</p>
    <p><svg class="ico"><use href="#i-globe"/></svg>www.tessaro-advisory.com</p>
  </div>
  <p class="copy">Copyright © 2021 Tessaro Advisory · All Rights Reserved</p>
</section>

</body>
</html>
```